Carver Lindqvist Group Business Cards

We have a new logo, and want to design new business cards with it. We are 21 years in business, and want a fresh but professional look, so not a lot of extra stuff on the card. We are a recruiting and staffing firm focused on placing accounting and finance professionals in the Dallas TX area. I've attached our new logo that should be displayed on the cards. Here is what I think we want on the cards:
Ray Pemberly, CPA
Partner and Managing Director
8282 Orchard Vale Rd.
Suite 610
Dallas, TX 75391
O 214-555-0184
M 214-555-0237
ray@carverlindqvist.example
www.carverlindqvist.example

```html
<!DOCTYPE html>
<html lang="en">
<head>
<meta charset="utf-8">
<title>Carver Lindqvist Group – Business Card</title>
<link rel="stylesheet" href="https://fonts.googleapis.com/css2?family=Roboto:wght@400;500;700&display=swap">
<style>
  :root {
    --page-bg: #e9e7e3;
    --card-white: #f7f7f7;
    --brand-blue: #4e6db2;
    --logo-blue: #2c4a9e;
    --text-light: #ffffff;
    --text-soft: #eef2fb;
  }
  html, body {
    margin: 0;
    width: 1200px;
    height: 900px;
    overflow: hidden;
    background: var(--page-bg);
    font-family: "Roboto", Arial, sans-serif;
  }
  .card {
    position: absolute;
    left: 100px;
    top: 165px;
    width: 1000px;
    height: 570px;
    display: flex;
    box-shadow: 0 10px 30px rgba(0,0,0,0.18);
  }
  .card-brand {
    width: 410px;
    background: var(--card-white);
    display: flex;
    align-items: center;
    justify-content: center;
  }
  .wordmark {
    display: flex;
    align-items: center;
    gap: 12px;
    color: var(--logo-blue);
    font-weight: 700;
    font-size: 25px;
    letter-spacing: 0.5px;
    text-transform: uppercase;
  }
  .wordmark-square {
    width: 18px;
    height: 18px;
    background: var(--logo-blue);
    flex: none;
  }
  .card-details {
    flex: 1;
    background: var(--brand-blue);
    color: var(--text-light);
    padding: 70px 0 0 70px;
    box-sizing: border-box;
  }
  .person-name {
    margin: 0;
    font-size: 27px;
    font-weight: 500;
    letter-spacing: 1px;
  }
  .person-title {
    margin: 4px 0 0;
    font-size: 17px;
    letter-spacing: 1px;
    color: var(--text-soft);
  }
  .contact-list {
    list-style: none;
    margin: 48px 0 0;
    padding: 0;
    font-size: 18px;
    letter-spacing: 1px;
    line-height: 1.45;
  }
  .contact-item {
    display: flex;
    align-items: flex-start;
    gap: 22px;
  }
  .contact-item.address { margin-bottom: 14px; }
  .contact-icon {
    width: 16px;
    height: 16px;
    margin-top: 4px;
    flex: none;
    fill: var(--text-light);
  }
</style>
</head>
<body>
  <div class="card">
    <div class="card-brand">
      <div class="wordmark">
        <span class="wordmark-square"></span>
        <span class="wordmark-name">Carver Lindqvist Group</span>
      </div>
    </div>
    <div class="card-details">
      <h1 class="person-name">Ray Pemberly, CPA</h1>
      <p class="person-title">Partner and Managing Director</p>
      <ul class="contact-list">
        <li class="contact-item address">
          <svg class="contact-icon" viewBox="0 0 16 16" aria-hidden="true"><path d="M8 0a5.5 5.5 0 0 0-5.5 5.5C2.5 9.6 8 16 8 16s5.5-6.4 5.5-10.5A5.5 5.5 0 0 0 8 0zm0 7.8a2.3 2.3 0 1 1 0-4.6 2.3 2.3 0 0 1 0 4.6z"/></svg>
          <span>8282 Orchard Vale Rd.<br>Suite 610<br>Dallas, TX 75391</span>
        </li>
        <li class="contact-item">
          <svg class="contact-icon" viewBox="0 0 16 16" aria-hidden="true"><path d="M3.6 1l2.3 3-1.3 1.6c.9 2 2.7 3.8 4.8 4.8L11 9.1l3 2.3-1.2 2.8C7 14 2 9 1.8 3.2z"/></svg>
          <span>214-555-0184</span>
        </li>
        <li class="contact-item">
          <svg class="contact-icon" viewBox="0 0 16 16" aria-hidden="true"><path d="M4.5 0h7A1.5 1.5 0 0 1 13 1.5v13a1.5 1.5 0 0 1-1.5 1.5h-7A1.5 1.5 0 0 1 3 14.5v-13A1.5 1.5 0 0 1 4.5 0zM5 2v10h6V2zm3 11a1 1 0 1 0 0 2 1 1 0 0 0 0-2z"/></svg>
          <span>214-555-0237</span>
        </li>
        <li class="contact-item">
          <svg class="contact-icon" viewBox="0 0 16 16" aria-hidden="true"><path d="M1 3h14v1.2L8 8.6 1 4.2zm0 2.6l7 4.4 7-4.4V13H1z"/></svg>
          <span>ray@carverlindqvist.example</span>
        </li>
        <li class="contact-item">
          <svg class="contact-icon" viewBox="0 0 16 16" aria-hidden="true"><circle cx="8" cy="8" r="7" fill="none" stroke="#fff" stroke-width="1.5"/><path d="M1 8h14M8 1c2.5 2.5 2.5 11.5 0 14M8 1c-2.5 2.5-2.5 11.5 0 14" fill="none" stroke="#fff" stroke-width="1.2"/></svg>
          <span>www.carverlindqvist.example</span>
        </li>
      </ul>
    </div>
  </div>
</body>
</html>
```